Horizzontal format 2 m long x 0,80 m high

We need a horizzontal format design for a rectangular board 2m long and 0,8 meter high.

The board will be positioned on a side of soccer fields, so the text should be readable for the other side of the field.
Color:text colors should be read, and grey.

Copy:
"Murovanti Impresa Edile.
Pensiamo a TUTTO NOI, dall'ideazione alla REALIZZAZIONE

Ristrutturazioni d'Interni ed Esterni,
Progettazione con la collaborazione di un TEAM DI ARCHITETTI E INGEGNERI
Realizzazione con materiali di altissimo livello (only if there is enough space!)
CURA DEI particolari per ottenere grandi risultati (only if there is enough space!)

TOTAL RELAX con Murovanti Impresa Edile"

CTA: Richiedi subito una consulenza gratui
Riferimenti:
3421857630
info@murovanti-esempio.it
murovanti-esempio.it
seguici su Facebook

Target Market(s)

Man & Woman 26+, medium income, house owners, soccer fans. The board will be showed during soccer games,

Industry/Entity Type

Construction Company

Colors
ec1f27
eaf1f7
f3f1f8
cedeed

Requirements
Must have
• Murovanti Logo.
• Charater text very big, it must be readable from the other side of a soccer filed.
• Text and services are the center of the requested design. Images are not necessary.
Nice to have
• It would be nice if play with differt background colors (almost grey and red, but you could use also other colors, like light grey for example!). We'd like not only "rectangular lines" to divide the spaces.

```html
<!DOCTYPE html>
<html lang="it">
<head>
<meta charset="utf-8">
<title>Murovanti Impresa Edile – Banner bordocampo</title>
<link rel="stylesheet" href="https://fonts.googleapis.com/css2?family=Anton&display=swap">
<style>
  :root{
    --red:#e3151d;
    --dark:#1d1d1d;
    --white:#ffffff;
    --grey:#bfc3c8;
    --stage:#2e5518;
  }
  *{margin:0;padding:0;box-sizing:border-box}
  html,body{width:1200px;height:927px;overflow:hidden;background:var(--stage)}
  .canvas{position:relative;width:1200px;height:927px}
  .banner{position:absolute;left:20px;top:231px;width:1160px;height:464px;overflow:hidden;
    font-family:"Anton",sans-serif;background:var(--white)}
  .banner-shapes{position:absolute;inset:0}
  .headline{position:absolute;left:27px;top:22px;color:var(--red);font-size:82px;
    line-height:1;letter-spacing:-0.5px;white-space:nowrap}
  .pill{position:absolute;left:27px;border-radius:40px;color:var(--white);
    display:flex;align-items:center;padding-left:18px;white-space:nowrap;line-height:1}
  .pill--services{top:129px;width:783px;height:71px;background:var(--dark);font-size:46px}
  .pill--relax{top:215px;width:754px;height:60px;background:var(--red);font-size:38px}
  .brand{position:absolute;left:880px;top:38px;display:flex;align-items:center;gap:14px}
  .brand-mark{width:52px;height:52px;background:var(--grey)}
  .brand-name{color:var(--red);font-size:42px;line-height:1}
  .contacts{position:absolute;left:27px;top:322px;display:flex;flex-direction:column;gap:26px}
  .contact-row{display:flex;align-items:center;gap:20px}
  .contact{display:flex;align-items:center;gap:8px;color:var(--red);font-size:30px;
    line-height:1;white-space:nowrap}
  .contact svg{width:36px;height:36px;flex:none}
</style>
</head>
<body>
<div class="canvas">
  <section class="banner">
    <svg class="banner-shapes" viewBox="0 0 1160 464" width="1160" height="464">
      <defs>
        <linearGradient id="officeTone" x1="0" y1="0" x2="1" y2="1">
          <stop offset="0" stop-color="#e9e7e2"/>
          <stop offset="0.45" stop-color="#e8c44a"/>
          <stop offset="1" stop-color="#6e6a66"/>
        </linearGradient>
        <radialGradient id="roomTone" cx="0.5" cy="0.4" r="0.7">
          <stop offset="0" stop-color="#f2f2f2"/>
          <stop offset="1" stop-color="#8b8f93"/>
        </radialGradient>
      </defs>
      <rect x="0" y="297" width="1160" height="167" fill="var(--dark)"/>
      <path d="M850 0 Q905 250 760 464 L1160 464 L1160 0 Z" fill="url(#officeTone)"
        role="img" aria-label="Fotografia di un ufficio ristrutturato con parete a griglia gialla"/>
      <rect x="800" y="0" width="360" height="146" fill="var(--white)"/>
      <path d="M850 0 Q905 250 760 464" fill="none" stroke="var(--red)" stroke-width="4"/>
      <circle cx="879" cy="207" r="64" fill="url(#roomTone)" stroke="var(--red)" stroke-width="4"
        role="img" aria-label="Fotografia di un soggiorno moderno"/>
      <circle cx="842" cy="333" r="50" fill="url(#roomTone)" stroke="var(--red)" stroke-width="4"
        role="img" aria-label="Fotografia di un interno luminoso con piante"/>
      <circle cx="788" cy="419" r="36" fill="url(#roomTone)" stroke="var(--red)" stroke-width="4"
        role="img" aria-label="Fotografia di una cucina moderna"/>
    </svg>

    <h1 class="headline">Murovanti Impresa Edile.</h1>
    <p class="pill pill--services">Ristrutturazioni d'Interni ed Esterni</p>
    <p class="pill pill--relax">TOTAL RELAX con Murovanti Impresa Edile</p>

    <div class="brand">
      <span class="brand-mark"></span>
      <span class="brand-name">MUROVANTI</span>
    </div>

    <div class="contacts">
      <div class="contact-row">
        <span class="contact">
          <svg viewBox="0 0 44 44"><circle cx="22" cy="22" r="21" fill="var(--red)"/>
            <path d="M15 11c2-1 3 0 4 2l2 4c.5 1.2 0 2-1 2.8l-1.3 1c1 2.6 2.8 4.4 5.4 5.4l1-1.3c.8-1 1.6-1.5 2.8-1l4 2c2 1 3 2 2 4-1.4 2.6-4 3.6-7 2.6-6.2-2-10.6-6.4-12.6-12.6-1-3 0-5.6 2.7-7z" fill="var(--dark)"/></svg>
          3421857630
        </span>
        <span class="contact">
          <svg viewBox="0 0 44 44" role="img" aria-label="Icona social"><circle cx="22" cy="22" r="21" fill="var(--red)"/></svg>
          seguici su
        </span>
      </div>
      <div class="contact-row">
        <span class="contact">
          <svg viewBox="0 0 44 44"><circle cx="22" cy="22" r="19.5" fill="none" stroke="var(--red)" stroke-width="3"/>
            <rect x="10" y="14" width="24" height="16" fill="none" stroke="var(--red)" stroke-width="2.6"/>
            <path d="M10 14 L22 24 L34 14" fill="none" stroke="var(--red)" stroke-width="2.6"/></svg>
          info@murovanti-esempio.it
        </span>
        <span class="contact">
          <svg viewBox="0 0 44 44"><circle cx="22" cy="22" r="19.5" fill="none" stroke="var(--red)" stroke-width="3"/>
            <ellipse cx="22" cy="22" rx="8" ry="19.5" fill="none" stroke="var(--red)" stroke-width="2.4"/>
            <path d="M3 22 H41 M6 13 H38 M6 31 H38" stroke="var(--red)" stroke-width="2.4"/></svg>
          murovanti-esempio.it
        </span>
      </div>
    </div>
  </section>
</div>
</body>
</html>
```